Business card for massage therapy company called Brook Fern Wellness

Need business card for massage therapy company called Brook Fern Wellness. Would like my logo on the front and the back of the card I have 3 options of logos and you can play with what looks better.

Would like this information displayed on the back of the card:

Marcus Ellery
Licensed Massage Therapist
321-555-0147
brookfern-example.com
brookfern_rest_

```html
<!DOCTYPE html>
<html lang="en">
<head>
<meta charset="utf-8">
<title>Brook Fern Wellness — Business Card</title>
<link href="https://fonts.googleapis.com/css2?family=Montserrat:wght@400;500&display=swap" rel="stylesheet">
<style>
  :root {
    --sage: #737a61;
    --paper: #ffffff;
    --backdrop: #e6e6e6;
  }
  html, body {
    margin: 0;
    padding: 0;
    width: 998px;
    height: 1200px;
    overflow: hidden;
    background: var(--backdrop);
    font-family: "Montserrat", sans-serif;
  }
  .canvas {
    position: relative;
    width: 998px;
    height: 1200px;
  }
  .card {
    position: absolute;
    left: 91px;
    width: 786px;
    height: 450px;
    overflow: hidden;
  }
  .card-front { top: 67px; background: var(--paper); }
  .card-back  { top: 624px; background: var(--sage); }

  .card svg.decor {
    position: absolute;
    inset: 0;
  }

  /* front */
  .front-wordmark {
    position: absolute;
    left: 0;
    right: 0;
    top: 278px;
    text-align: center;
    color: var(--sage);
    font-weight: 400;
    font-size: 30px;
    letter-spacing: 4px;
    text-transform: uppercase;
  }

  /* back */
  .back-seal-name {
    position: absolute;
    left: 75px;
    top: 210px;
    width: 240px;
    text-align: center;
    color: var(--sage);
    font-weight: 400;
    font-size: 22px;
    letter-spacing: 3px;
    text-transform: uppercase;
  }
  .back-wordmark {
    position: absolute;
    right: 34px;
    top: 60px;
    width: 300px;
    text-align: center;
    color: var(--paper);
    font-weight: 400;
    font-size: 22px;
    line-height: 1.45;
    letter-spacing: 4px;
    text-transform: uppercase;
  }
  .divider {
    position: absolute;
    left: 418px;
    top: 66px;
    width: 4px;
    height: 319px;
    background: var(--paper);
    opacity: 0.85;
  }
  .contact {
    position: absolute;
    right: 34px;
    top: 232px;
    margin: 0;
    padding: 0;
    list-style: none;
    text-align: right;
    color: var(--paper);
    font-weight: 400;
    font-size: 17px;
    line-height: 25px;
    text-transform: uppercase;
  }
</style>
</head>
<body>
<main class="canvas">

  <section class="card card-front" aria-label="Card front">
    <svg class="decor" width="786" height="450" viewBox="0 0 786 450">
      <circle cx="393" cy="165" r="69" fill="none" stroke="var(--sage)" stroke-width="2"/>
      <polygon points="0,396 164,396 143,418 0,418" fill="var(--sage)"/>
      <polygon points="196,396 786,396 786,418 175,418" fill="var(--sage)"/>
    </svg>
    <div class="front-wordmark">Brook Fern Wellness</div>
  </section>

  <section class="card card-back" aria-label="Card back">
    <svg class="decor" width="786" height="450" viewBox="0 0 786 450">
      <circle cx="210" cy="226" r="236" fill="none" stroke="var(--paper)" stroke-width="28"/>
      <circle cx="210" cy="226" r="162" fill="var(--paper)"/>
      <circle cx="195" cy="224" r="119" fill="none" stroke="var(--sage)" stroke-width="2"/>
    </svg>
    <div class="back-seal-name">Brook Fern</div>
    <div class="divider"></div>
    <div class="back-wordmark">Brook Fern<br>Wellness</div>
    <ul class="contact">
      <li>Marcus Ellery</li>
      <li>Licensed Massage Therapist</li>
      <li>321-555-0147</li>
      <li>brookfern-example.com</li>
      <li>brookfern_rest_</li>
    </ul>
  </section>

</main>
</body>
</html>
```